Bramble Peak Information Technology Business Card
Services for Move Add Change, Technical Relocation, Server Room Support, Technical Support
Bramble Peak Information Technology Business Card - Information Technology
Creative Brief
Professional
Owen Darlisk
2917 41st Lane Northeast Seattle WA 98422
owen@bramblepkit-example.com
www.bramblepkit-example.com
The original logo on the back, #34 and #35
Move Add and Changes, Corporate Relocation, Server Room Support, Technical Support

```html
<!DOCTYPE html>
<html lang="en">
<head>
<meta charset="utf-8">
<title>Bramble Peak Information Technology Stationery</title>
<link rel="stylesheet" href="https://fonts.googleapis.com/css2?family=Montserrat:wght@400;600;800&display=swap">
<style>
  :root {
    --bg: #e8e8e8;
    --paper: #ffffff;
    --ink: #3a3a3a;
    --ink-soft: #6d6d6d;
    --band: #3b3b3b;
    --accent: #f39a1e;
  }
  * { box-sizing: border-box; margin: 0; padding: 0; }
  html, body { width: 1200px; height: 937px; overflow: hidden; }
  body {
    background: var(--bg);
    font-family: "Montserrat", Arial, sans-serif;
    color: var(--ink);
    position: relative;
  }
  .sheet {
    position: absolute;
    background: var(--paper);
    overflow: hidden;
  }
  .wave {
    position: absolute;
    left: 0; bottom: 0;
    width: 100%;
    display: block;
  }
  .wave .band { fill: var(--band); }
  .wave .line { fill: none; stroke: var(--accent); }

  .brand {
    display: inline-flex;
    align-items: center;
    font-weight: 800;
    color: var(--ink);
    letter-spacing: 0.02em;
    white-space: nowrap;
    line-height: 1;
  }
  .brand .dot {
    display: inline-block;
    border-radius: 50%;
    background: var(--accent);
  }

  /* Letterhead */
  .letterhead { left: 182px; top: 56px; width: 385px; height: 552px; }
  .letterhead .brand { position: absolute; left: 30px; top: 38px; font-size: 17px; gap: 6px; }
  .letterhead .brand .dot { width: 10px; height: 10px; }
  .letterhead .sender {
    position: absolute; right: 26px; top: 22px;
    font-size: 5.5px; line-height: 1.5; text-align: right; color: var(--ink-soft);
  }
  .letter {
    position: absolute; left: 30px; top: 96px; width: 320px;
    font-size: 5.6px; line-height: 1.6; color: var(--ink-soft);
  }
  .letter p { margin-bottom: 8px; }
  .signature {
    width: 40px; height: 16px; margin: 4px 0 4px;
    background: linear-gradient(90deg, #9a9a9a, #d0d0d0);
    border-radius: 8px;
  }
  .letterhead .wave { height: 92px; }

  /* Presentation folder */
  .folder { left: 633px; top: 38px; width: 458px; height: 577px; }
  .folder .brand {
    position: absolute; left: 0; right: 0; top: 318px;
    justify-content: center; font-size: 40px; gap: 12px;
  }
  .folder .brand .dot { width: 24px; height: 24px; }
  .folder .wave { height: 150px; }

  /* Business cards */
  .card { left: 43px; width: 202px; height: 101px; }
  .card-front { top: 663px; }
  .card-back { top: 785px; }
  .card-front .brand { position: absolute; left: 12px; top: 22px; font-size: 10px; gap: 4px; }
  .card-front .brand .dot { width: 6px; height: 6px; }
  .card-front .contact {
    position: absolute; left: 112px; top: 14px;
    font-size: 4.3px; line-height: 1.55; color: var(--ink-soft);
  }
  .card-front .contact .name { font-weight: 600; color: var(--ink); font-size: 5px; }
  .card-front .wave { height: 34px; }
  .card-back .brand {
    position: absolute; left: 0; right: 0; top: 43px;
    justify-content: center; font-size: 13px; gap: 5px;
  }
  .card-back .brand .dot { width: 8px; height: 8px; }

  /* Envelope front */
  .envelope-front { left: 263px; top: 673px; width: 436px; height: 208px; }
  .envelope-front .brand { position: absolute; left: 20px; top: 26px; font-size: 14px; gap: 5px; }
  .envelope-front .brand .dot { width: 8px; height: 8px; }
  .envelope-front .wave { height: 70px; }

  /* Envelope back */
  .envelope-back { left: 739px; top: 673px; width: 408px; height: 218px; }
  .envelope-back .flap { position: absolute; left: 0; top: 0; width: 100%; height: 96px; display: block; }
  .envelope-back .flap path { fill: var(--band); }
  .envelope-back .web {
    position: absolute; left: 0; right: 0; top: 26px;
    text-align: center; color: #ffffff; font-size: 9px; letter-spacing: 0.14em;
  }
</style>
</head>
<body>

<!-- Letterhead -->
<section class="sheet letterhead">
  <div class="brand"><span>BRAMBLE PEAK</span><span class="dot"></span></div>
  <div class="sender">
    Owen Darlisk<br>
    2917 41st Lane Northeast<br>
    Seattle WA 98422<br>
    206.555.0148<br>
    owen@bramblepkit-example.com
  </div>
  <div class="letter">
    <p>June 4, 2024</p>
    <p>Dear Client,<br>Recipient Name, Company Office, City State</p>
    <p>Thank you for choosing our team for your office move. We plan each relocation with care so your servers, desks and phones are ready on day one. Our technicians handle cabling, setup and testing while your staff keeps working.</p>
    <p>Our server room support keeps systems cool, tidy and secure, with clear records of every change we make.</p>
    <p>Please reach out with any questions about moves, adds, changes or day to day technical support.</p>
    <p>Best regards,</p>
    <div class="signature" role="img" aria-label="Handwritten signature"></div>
    <p>Owen Darlisk<br>Director</p>
  </div>
  <svg class="wave" viewBox="0 0 100 24" preserveAspectRatio="none" aria-hidden="true">
    <path class="band" d="M0 12 Q55 -2 100 6 L100 24 L0 24 Z"/>
    <path class="line" d="M0 8.5 Q55 -5 100 2.5" stroke-width="0.6"/>
  </svg>
</section>

<!-- Presentation folder -->
<section class="sheet folder">
  <div class="brand"><span>BRAMBLE PEAK</span><span class="dot"></span></div>
  <svg class="wave" viewBox="0 0 100 33" preserveAspectRatio="none" aria-hidden="true">
    <path class="band" d="M0 16 Q55 0 100 8 L100 33 L0 33 Z"/>
    <path class="line" d="M0 12 Q55 -4 100 4" stroke-width="0.5"/>
  </svg>
</section>

<!-- Business card front -->
<section class="sheet card card-front">
  <div class="brand"><span>BRAMBLE PEAK</span><span class="dot"></span></div>
  <div class="contact">
    <div class="name">Owen Darlisk</div>
    Director<br>
    206.555.0148<br>
    owen@bramblepkit-example.com<br>
    www.bramblepkit-example.com<br>
    2917 41st Lane Northeast<br>
    Seattle WA 98422
  </div>
  <svg class="wave" viewBox="0 0 100 17" preserveAspectRatio="none" aria-hidden="true">
    <path class="band" d="M0 10 Q55 0 100 5 L100 17 L0 17 Z"/>
    <path class="line" d="M0 7 Q55 -3 100 2" stroke-width="0.6"/>
  </svg>
</section>

<!-- Business card back -->
<section class="sheet card card-back">
  <div class="brand"><span>BRAMBLE PEAK</span><span class="dot"></span></div>
</section>

<!-- Envelope front -->
<section class="sheet envelope-front">
  <div class="brand"><span>BRAMBLE PEAK</span><span class="dot"></span></div>
  <svg class="wave" viewBox="0 0 100 16" preserveAspectRatio="none" aria-hidden="true">
    <path class="band" d="M0 9 Q55 0 100 5 L100 16 L0 16 Z"/>
    <path class="line" d="M0 6 Q55 -3 100 2" stroke-width="0.4"/>
  </svg>
</section>

<!-- Envelope back -->
<section class="sheet envelope-back">
  <svg class="flap" viewBox="0 0 100 24" preserveAspectRatio="none" aria-hidden="true">
    <path d="M0 0 L100 0 L100 6 Q50 30 0 6 Z"/>
  </svg>
  <div class="web">www.bramblepkit-example.com</div>
</section>

</body>
</html>
```